Seminar Flyer

We would like a flyer describing a seminar we will be presenting to window cleaners. The seminar topic is Glass Restoration and will include discussions on types of glass, types of glass damage and solutions. I am including the following (sample) description:
"Spend a day with The PaneMaven and learn how you can benefit from learning "Glass Restoration" and the many benefits to offering this service to your clients.
Before investing a lot of "time and money" in ANY Glass Restoration System, learn what Glass Restoration is all about and how you can turn a small investment into a very profitable business. And, this new business can be easily expanded into several other related business's.
Ready to expand your business and make some great money?
"DON'T WAIT" - Start offering your clients Glass Restoration Services.
"Glass Restoration" is one of the most profitable "Add-On" businesses for the window cleaning industry and you now have an opportunity to learn from one of the industry
leaders. Lyle Brandt will be offering a full day "hands-on" seminar on Glass Restoration.
The seminar will cover:
Glass Types
Glass Damage
Glass Coatings
Glass Distortion & Breakage
Glass Restoration Systems
Glass Restoration Procedures
Customer Expectations
Marketing and Pricing a job
Hands on demonstrations
And much much more.....
And did I mention it will cover "Glass"?
This full day seminar will be presented by Lyle Brandt and sponsored by the H.Morwick Company at their facility in Carson, California.
Space will be limited, so you must register to attend, but the seminar and lunch is FREE.
This all day seminar will also cover discussions on:
Hard Water Spot Removal and methods for removing.
What exactly is "Tin Etch Haze" and how to prevent or remove it easily.
Minor scratch removal (light scratches and metal marks)
Tempered Glass Defects - Waivers and precautions
Excess Scratch removal (tempered Glass scratching)
Graffiti Removal (major scratch and acid etch damage)
Additional Money Makers:
Anti-Graffiti Film Application
- An easy add on business for glass restoration businesses
Hard Water Spot Removal and Glass Sealant
- An easy add on business for window cleaning businesses
Window Frame Restoration and Treatment
- An easy add on business for window cleaning businesses"
Lyle Brandt, the President of The Brandt Company, is well known in the window cleaning industry as "PaneMaven", so we want to make sure that branding is included in the flyer.
PLEASE NOTE: The flyer will be distributed as an e-mail attachment so the flyer itself will not have any specific information regarding dates and location.
Target Market(s)
Window Cleaners; small business owners.
Industry/Entity Type
Window Cleaning

```html
<!DOCTYPE html>
<html lang="en">
<head>
<meta charset="utf-8">
<title>Glass Restoration Seminar</title>
<link rel="stylesheet" href="https://fonts.googleapis.com/css2?family=Anton&family=Arimo:ital,wght@0,400;0,700;1,700&family=Archivo+Black&family=Cormorant+SC:wght@700&display=swap">
<style>
:root{
  --blue-deep:#0a3a9e;
  --blue-mid:#1f74d8;
  --blue-light:#8fe0ff;
  --red:#d2140f;
  --red-dark:#a60c08;
  --ink:#000;
  --paper:#fff;
  --panel:rgba(255,255,255,.78);
}
*{box-sizing:border-box;margin:0;padding:0}
html,body{width:927px;height:1200px;overflow:hidden}
body{font-family:"Arimo",Arial,sans-serif;color:var(--ink);background:var(--blue-deep)}
.flyer{position:relative;width:927px;height:1200px;overflow:hidden;
  background:
    radial-gradient(ellipse 420px 260px at 470px 520px,rgba(220,250,255,.9),rgba(140,220,255,0) 70%),
    radial-gradient(ellipse 300px 500px at 820px 620px,rgba(160,235,255,.7),rgba(160,235,255,0) 70%),
    radial-gradient(ellipse 380px 260px at 220px 420px,rgba(120,200,255,.6),rgba(120,200,255,0) 70%),
    linear-gradient(160deg,var(--blue-deep) 0%,var(--blue-mid) 30%,#45b4f0 55%,var(--blue-mid) 75%,var(--blue-deep) 100%);}
.presenter-banner{position:absolute;left:133px;top:12px;width:662px;height:56px;background:var(--red);
  color:var(--paper);font-family:"Cormorant SC",Georgia,serif;font-weight:700;font-size:40px;letter-spacing:1px;
  display:flex;align-items:center;justify-content:center}
.title{position:absolute;left:0;top:78px;width:927px;text-align:center;font-family:"Anton",Impact,sans-serif;
  font-size:102px;line-height:1.08;color:var(--paper);letter-spacing:3px;text-shadow:4px 5px 4px rgba(0,0,0,.85)}
.intro{position:absolute;left:110px;top:190px;width:707px;text-align:center;font-weight:700;font-size:15px;line-height:1.15}
.gallery{position:absolute;left:8px;top:255px;width:909px;height:227px}
.shot{position:absolute;top:0;width:296px;height:227px;background:#000;padding:9px}
.shot .photo{width:100%;height:100%}
.shot .num{position:absolute;left:9px;top:9px;width:40px;height:46px;background:#000;color:var(--paper);
  font-family:"Archivo Black",Arial,sans-serif;font-size:34px;display:flex;align-items:center;justify-content:center}
.shot-1{left:0}.shot-2{left:307px}.shot-3{left:613px}
.shot-1 .photo{background:linear-gradient(135deg,#6c7480,#c9cfd6 45%,#4c535c)}
.shot-2 .photo{background:linear-gradient(135deg,#3e4650,#b7c0c8 50%,#58606a)}
.shot-3 .photo{background:linear-gradient(135deg,#59626c,#d6dde3 50%,#4a525b)}
.callout{position:absolute;left:0;top:490px;width:927px;text-align:center;font-family:"Archivo Black",Arial,sans-serif;
  font-size:27px;color:var(--red);-webkit-text-stroke:1px var(--paper);text-shadow:2px 2px 2px rgba(0,0,0,.5)}
.callout-sub{position:absolute;left:0;top:528px;width:927px;text-align:center;font-size:20px;line-height:1.2}
.panel{position:absolute;left:8px;width:522px;background:var(--panel);border-radius:6px;
  box-shadow:0 0 8px rgba(255,255,255,.6)}
.panel-about{top:568px;height:205px;padding:18px 22px;font-size:14px;line-height:1.25;text-align:center}
.panel-about p+p{margin-top:16px}
.panel-topics{top:798px;height:331px;padding:22px 16px;font-size:13.5px;font-weight:700;line-height:1.45}
.panel-topics h2{font-size:17px;line-height:1.3}
.panel-topics h3{font-size:15.5px;margin-top:12px;line-height:1.6}
.panel-topics ul{list-style:none}
.panel-topics .extras li{margin-bottom:9px;font-size:13px}
.notice{position:absolute;left:538px;top:568px;width:379px;height:144px;background:var(--red);color:var(--paper);
  text-align:center;padding:8px 10px;font-size:16px;line-height:1.2}
.notice strong{display:block;font-family:"Arimo",Arial,sans-serif;font-weight:700;font-size:30px;line-height:1.15}
.notice .big{font-weight:700;font-size:22px}
.learn{position:absolute;left:564px;top:733px;width:340px}
.learn h2{font-size:25px;font-weight:700;margin-bottom:8px}
.learn ul{list-style:none;font-size:18.5px;line-height:30.5px}
.footer-bar{position:absolute;left:0;top:1133px;width:927px;height:57px;background:#000;color:var(--paper);
  font-size:23px;display:flex;align-items:center;justify-content:center}
</style>
</head>
<body>
<div class="flyer">
  <div class="presenter-banner">The PaneMaven Presents</div>
  <h1 class="title">GLASS RESTORATION</h1>
  <p class="intro">Glass Restoration is one of the most profitable "Add-On" businesses for the window cleaning industry and you now have an opportunity to learn from one of the industry leaders.</p>

  <div class="gallery">
    <div class="shot shot-1"><div class="photo" role="img" aria-label="Storefront window covered in scratched graffiti"></div><span class="num">1</span></div>
    <div class="shot shot-2"><div class="photo" role="img" aria-label="Storefront window during glass restoration, damaged area being polished"></div><span class="num">2</span></div>
    <div class="shot shot-3"><div class="photo" role="img" aria-label="Storefront window after restoration, clear glass"></div><span class="num">3</span></div>
  </div>

  <p class="callout">Ready to expand your business and&nbsp; make some great money?</p>
  <p class="callout-sub">DON'T WAIT - Start offering your clients Glass Restoration Services.</p>

  <div class="panel panel-about">
    <p>Spend a day with The PaneMaven and learn how you can benefit from learning "Glass Restoration" and the many benefits to offering this service to your clients.</p>
    <p>Before investing a lot of&nbsp; time and money in ANY Glass Restoration System, learn what Glass Restoration is all about and how you can turn a small investment into a very profitable business. And, this new business can be easily expanded into several other related businesses.</p>
  </div>

  <div class="notice">
    <strong>Space will be limited,</strong>
    so you must register to attend, but the <span class="big">seminar and lunch are FREE.</span>
  </div>

  <div class="learn">
    <h2>Learn About:</h2>
    <ul>
      <li>Glass Types</li>
      <li>Glass Damage</li>
      <li>Glass Coatings</li>
      <li>Glass Distortion &amp; Breakage</li>
      <li>Glass Restoration Systems</li>
      <li>Glass Restoration Procedures</li>
      <li>Customer Expectations</li>
      <li>Marketing and Pricing a job</li>
      <li>Hands on demonstrations</li>
      <li>And much much more.....</li>
    </ul>
  </div>

  <div class="panel panel-topics">
    <h2>This all day seminar will also cover discussions on:</h2>
    <ul>
      <li>Hard Water Spot Removal and methods for removing.</li>
      <li>What exactly is "Tin Etch Haze" and how to prevent or remove it easily.</li>
      <li>Minor scratch removal (light scratches and metal marks)</li>
      <li>Tempered Glass Defects - Waivers and precautions</li>
      <li>Excess scratch removal (tempered glass scratching)</li>
      <li>Graffiti Removal (major scratch and acid etch damage)</li>
    </ul>
    <h3>Additional Money Makers:</h3>
    <ul class="extras">
      <li>Anti-Graffiti Film Application</li>
      <li>Hard Water Spot Removal and Glass Sealant</li>
      <li>Window Frame Restoration and Treatment</li>
    </ul>
  </div>

  <div class="footer-bar">This full day seminar will be presented by Lyle Brandt, The PaneMaven</div>
</div>
</body>
</html>
```